Korvix App Graphics Design

Our application promotes location based self expression via pictures and text. The primary focus of the application is on the content posted and not on the person that posted it.

We want a very clean and fresh design that evokes positive energy. Our site is unique so our design should be as well. People will reveal thoughts on our site, so the design should convey a "revealing" feel. Our site is a place where people are comfortable to freely express themselves. Colors we have in mind are blue and green hues with earth tones for background.

Our project is to design ten screens for our Korvix application at resolution of 1136-by-640 pixels:

Feed Screen
Camera Screen
Post Screen
Check In Screen
Approval Screen
Map Screen
Flag Screen
Feed Select Screen
Export Screen
Menu Screen

In the contest phase we will require only three screens to be submitted. The screens we require to be submitted are: Feed Screen; Map Screen and Camera Screen. The designer we select as the winner of the competition will then complete the project and deliver a total of the ten screens described above in the handover phase.

We have attached a document below with detailed specs of each screen, we ask for your innovation to bring these screens to life through your design.
Updates

We want to clarify one aspect regarding the VISOR: the visor needs to be transparent so that when the picture scrolls underneath it, you can still see the picture underneath the visor.

Hi Everyone,

We have noticed that some designers need clarification regarding the visor element in the feed screen.
I have attached two examples to our brief area called:
Visor Example 1 and Visor Example 2

Please note that these are not the style we are looking for but are a good example to the concept of a Transparent Visor above the feed stream. We are looking for you guys to come up with a Visor concept that is consistent with the style of the design you are submitting.

Thanks,

Bo

Target Market(s)

People 17-40 who want to share their thought about the world around them.

Industry/Entity Type

Flag

Font styles to use
Sans Serif
Other font styles liked:
• We like “Helvetica New” or “Avenir” but are flexible

Requirements
Must have
• Visor component should look innovative.

```html
<!DOCTYPE html>
<html lang="en">
<head>
<meta charset="utf-8">
<title>Korvix App Screens</title>
<link rel="stylesheet" href="https://fonts.googleapis.com/css2?family=Arimo:wght@400;600;700&display=swap">
<style>
:root{
  --bg:#e8edec;
  --blue:#0d7af3;
  --blue-dark:#0a66cc;
  --white:#ffffff;
  --ink:#1b1b1b;
  --grey:#8e8e93;
  --line:#dcdcdf;
  --row:#f2f2f4;
  --search:#c9c9ce;
  --map:#ece7da;
  --black:#000000;
  --red:#e5302a;
}
*{box-sizing:border-box;margin:0;padding:0}
html,body{width:1200px;height:1000px;overflow:hidden}
body{background:radial-gradient(ellipse at 50% 40%,#f4f7f6 0%,var(--bg) 75%);font-family:"Arimo",Helvetica,Arial,sans-serif;position:relative;color:var(--ink)}
.screen{position:absolute;top:235px;width:286px;height:507px;background:var(--white);overflow:hidden;box-shadow:0 6px 24px rgba(0,0,0,.12)}
.screen--feed{left:80px}
.screen--map{left:460px}
.screen--photo{left:839px}
.abs{position:absolute}
.status{top:0;left:0;width:100%;height:20px;background:var(--blue);color:var(--white);font-size:11px;display:flex;align-items:center;justify-content:space-between;padding:0 7px}
.status__time{position:absolute;left:0;right:0;text-align:center;font-weight:600}
.status__right{display:flex;align-items:center;gap:4px}
.battery{width:22px;height:10px;border:1px solid var(--white);border-radius:2px;padding:1px}
.battery span{display:block;width:100%;height:100%;background:var(--white)}
.navbar{top:20px;left:0;width:100%;height:42px;background:var(--blue);color:var(--white);display:flex;align-items:center;justify-content:center}
.navbar__title{font-size:15px;font-weight:600}
.navbar__left{position:absolute;left:10px;top:11px;display:flex;align-items:center;gap:4px;font-size:15px}
.navbar__right{position:absolute;right:10px;top:11px}
/* feed */
.feed-photo{top:62px;left:0;width:100%;height:300px;background:linear-gradient(180deg,#5f6f7d 0%,#a4806a 18%,#6a5a52 30%,#2b2a2c 38%,#5a4a42 48%,#3c332f 75%,#2a2321 88%,#4a3a30 100%)}
.visor{top:62px;left:0;width:100%;height:46px;background:rgba(180,205,230,.35);border-bottom:1px solid rgba(255,255,255,.5);color:var(--white);display:flex;align-items:center;justify-content:center;font-size:16px}
.visor__flag{position:absolute;left:10px;top:13px}
.visor__share{position:absolute;right:10px;top:14px}
.feed-meta{top:340px;left:9px;right:9px;display:flex;justify-content:space-between;color:var(--white);font-size:11px}
.vote-bar{top:362px;left:0;width:100%;height:39px;background:var(--blue);display:flex;color:var(--white);font-size:15px}
.vote-bar__btn{flex:1;display:flex;align-items:center;justify-content:center;gap:12px}
.vote-bar__btn + .vote-bar__btn{border-left:1px solid rgba(255,255,255,.5)}
.place{top:401px;left:0;width:100%;height:52px;background:var(--row);display:flex;align-items:center;padding-left:10px;gap:12px;font-size:11px}
.place__name{font-weight:600;margin-bottom:3px}
.feed-actions{top:453px;left:0;width:100%;height:54px;display:flex;align-items:center;justify-content:space-between;padding:0 16px}
.btn-primary{background:var(--blue);color:var(--white);font-size:15px;width:172px;height:32px;border-radius:3px;display:flex;align-items:center;justify-content:center}
.hash{color:var(--blue);font-size:24px;font-weight:700}
/* map */
.loc-row{left:0;width:100%;height:39px;background:var(--white);display:flex;align-items:center;font-size:15px;padding-left:20px;gap:18px;border-bottom:1px solid var(--line)}
.loc-row__chev{position:absolute;right:12px;color:#b9b9bd;font-size:16px}
.search-strip{top:180px;left:0;width:100%;height:40px;background:var(--search);padding:7px 6px}
.search-field{background:var(--white);height:26px;border-radius:4px;display:flex;align-items:center;justify-content:center;gap:5px;color:var(--grey);font-size:13px}
.map-area{top:220px;left:0;width:100%;height:250px;background:linear-gradient(135deg,#eee9dd,#e6e0d2 60%,#ede8dc)}
.callout{top:265px;left:68px;width:195px;height:40px;background:var(--white);border-radius:4px;display:flex;overflow:hidden;box-shadow:0 1px 4px rgba(0,0,0,.25)}
.callout__eta{width:40px;background:var(--blue);color:var(--white);font-size:8px;display:flex;flex-direction:column;align-items:center;justify-content:center;gap:2px}
.callout__addr{flex:1;display:flex;align-items:center;padding-left:12px;font-size:15px}
.map-actions{top:470px;left:0;width:100%;height:37px;background:var(--blue);display:flex;color:var(--white);font-size:15px}
.map-actions div{flex:1;display:flex;align-items:center;justify-content:center}
.map-actions div + div{border-left:1px solid rgba(255,255,255,.5)}
/* photo */
.viewfinder{top:62px;left:0;width:100%;height:286px;background:var(--black)}
.capture{top:103px;left:0;width:100%;height:207px;background:linear-gradient(180deg,#5d6a74 0%,#a07e68 22%,#5d4f4a 38%,#2c2a2b 46%,#5a4a40 60%,#3a302a 85%,#2b2420 100%)}
.filters{top:348px;left:0;width:100%;height:75px;background:var(--white);display:flex;gap:5px;padding:11px 11px 0}
.filter{width:40px;text-align:center;font-size:9px;color:var(--grey)}
.filter__thumb{width:40px;height:40px;border-radius:4px;margin-bottom:6px}
.filter--active{color:var(--blue);font-weight:600}
.tools{top:423px;left:0;width:100%;height:84px;background:var(--blue)}
.tool{position:absolute;top:25px;width:34px;height:34px;border-radius:50%;background:var(--white);display:flex;align-items:center;justify-content:center}
.shutter{position:absolute;left:112px;top:10px;width:64px;height:64px;border-radius:50%;border:1px solid rgba(255,255,255,.7);display:flex;align-items:center;justify-content:center}
.shutter span{width:52px;height:52px;border-radius:50%;background:var(--white);display:flex;align-items:center;justify-content:center}
</style>
</head>
<body>

<!-- Feed -->
<section class="screen screen--feed">
  <div class="abs status"><span>●●●○○ LUMA</span><span class="status__time">4:21 PM</span><span class="status__right">100% <span class="battery"><span></span></span></span></div>
  <header class="abs navbar">
    <svg class="navbar__left" width="18" height="18" viewBox="0 0 18 18"><path d="M1 4h16M1 9h16M1 14h16" stroke="#fff" stroke-width="2"/></svg>
    <span class="navbar__title">Feed Name</span>
    <svg class="navbar__right" width="20" height="20" viewBox="0 0 20 20"><circle cx="8" cy="8" r="6" fill="none" stroke="#fff" stroke-width="2"/><path d="M12.5 12.5l5.5 5.5" stroke="#fff" stroke-width="2.4"/></svg>
  </header>
  <div class="abs feed-photo" role="img" aria-label="Post photo: dusk sky over mountains and a calm lake"></div>
  <div class="abs visor">
    <svg class="visor__flag" width="16" height="20" viewBox="0 0 16 20"><path d="M2 1v18" stroke="#fff" stroke-width="2"/><path d="M3 2h11l-3 4 3 4H3z" fill="#fff"/></svg>
    Peace
    <svg class="visor__share" width="20" height="16" viewBox="0 0 20 16"><path d="M12 1l7 6-7 6V9C6 9 3 11 1 15 1 9 5 5 12 5z" fill="#fff"/></svg>
  </div>
  <div class="abs feed-meta"><span>9.1 mi</span><span>★ 200</span><span>3 hours ago</span></div>
  <div class="abs vote-bar">
    <div class="vote-bar__btn">Promote
      <svg width="22" height="22" viewBox="0 0 22 22"><circle cx="11" cy="11" r="11" fill="#fff"/><path d="M6 11l3.5 3.5L16 8" fill="none" stroke="#0d7af3" stroke-width="2.2"/></svg>
    </div>
    <div class="vote-bar__btn">
      <svg width="22" height="22" viewBox="0 0 22 22"><circle cx="11" cy="11" r="11" fill="#fff"/><path d="M7.5 7.5l7 7M14.5 7.5l-7 7" stroke="#0d7af3" stroke-width="2.2"/></svg>Demote
    </div>
  </div>
  <div class="abs place">
    <svg width="22" height="22" viewBox="0 0 22 22"><circle cx="11" cy="11" r="9" fill="none" stroke="#a8a8ad" stroke-width="1.5"/><path d="M4 18l9-5-5-5z" fill="#a8a8ad"/><path d="M18 4l-5 9-5-5z" fill="#c6c6cb"/></svg>
    <div><div class="place__name">Maple Grill</div><div>88 Elm Street, Fairview, NY 10231</div></div>
  </div>
  <div class="abs feed-actions">
    <svg width="22" height="18" viewBox="0 0 22 18"><rect x="1" y="4" width="20" height="13" rx="3" fill="#0d7af3"/><rect x="7" y="1" width="8" height="4" rx="1" fill="#0d7af3"/><circle cx="11" cy="10.5" r="4" fill="#fff"/><circle cx="11" cy="10.5" r="2.3" fill="#0d7af3"/></svg>
    <div class="btn-primary">Next Picture</div>
    <span class="hash">#</span>
  </div>
</section>

<!-- Map -->
<section class="screen screen--map">
  <div class="abs status"><span>●●●○○ LUMA</span><span class="status__time">4:21 PM</span><span class="status__right">100% <span class="battery"><span></span></span></span></div>
  <header class="abs navbar">
    <span class="navbar__left"><svg width="10" height="18" viewBox="0 0 10 18"><path d="M9 1L1 9l8 8" fill="none" stroke="#fff" stroke-width="2.2"/></svg>Back</span>
    <span class="navbar__title">Map</span>
  </header>
  <div class="abs loc-row" style="top:62px"><svg width="14" height="24" viewBox="0 0 14 24"><path d="M7 9L1 23" stroke="#9a9a9f" stroke-width="1.4"/><circle cx="8" cy="6" r="5" fill="#0d7af3"/></svg>Location<span class="loc-row__chev">›</span></div>
  <div class="abs loc-row" style="top:101px"><svg width="14" height="24" viewBox="0 0 14 24"><path d="M7 9L1 23" stroke="#9a9a9f" stroke-width="1.4"/><circle cx="8" cy="6" r="5" fill="#0d7af3"/></svg>Location<span class="loc-row__chev">›</span></div>
  <div class="abs loc-row" style="top:141px"><svg width="14" height="24" viewBox="0 0 14 24"><path d="M7 9L1 23" stroke="#9a9a9f" stroke-width="1.4"/><circle cx="8" cy="6" r="5" fill="#0d7af3"/></svg>Location<span class="loc-row__chev">›</span></div>
  <div class="abs search-strip"><div class="search-field"><svg width="11" height="11" viewBox="0 0 11 11"><circle cx="4.5" cy="4.5" r="3.5" fill="none" stroke="#8e8e93" stroke-width="1.3"/><path d="M7 7l3 3" stroke="#8e8e93" stroke-width="1.3"/></svg>Search</div></div>
  <div class="abs map-area" role="img" aria-label="Street map of a downtown neighbourhood"></div>
  <svg class="abs" style="top:0;left:0" width="286" height="470" viewBox="0 0 286 470">
    <circle cx="166" cy="348" r="37" fill="rgba(13,122,243,.06)" stroke="#0d7af3" stroke-width="1.5"/>
    <circle cx="134" cy="347" r="9" fill="#0d7af3" stroke="#fff" stroke-width="1.5"/>
    <path d="M166 322v22" stroke="#7a7a7a" stroke-width="1.5"/>
    <circle cx="166" cy="320" r="6" fill="#e5302a"/>
  </svg>
  <div class="abs callout">
    <div class="callout__eta"><svg width="18" height="12" viewBox="0 0 18 12"><path d="M3 5l2-4h8l2 4h2v5h-2v2h-3v-2H6v2H3v-2H1V5z" fill="#fff"/></svg>8 min</div>
    <div class="callout__addr">421 Location Ave<span class="loc-row__chev" style="right:10px">›</span></div>
  </div>
  <div class="abs map-actions"><div>Drop Pin</div><div>Current Location</div></div>
</section>

<!-- Photo -->
<section class="screen screen--photo">
  <div class="abs status"><span>●●●○○ LUMA</span><span class="status__time">4:21 PM</span><span class="status__right">100% <span class="battery"><span></span></span></span></div>
  <header class="abs navbar">
    <svg class="abs" style="left:21px;top:11px" width="20" height="20" viewBox="0 0 20 20"><rect width="20" height="20" rx="2" fill="#fff"/><path d="M11 3L6 11h4l-1 6 5-8h-4z" fill="#0d7af3"/></svg>
    <svg class="abs" style="left:67px;top:11px" width="20" height="20" viewBox="0 0 20 20"><path d="M16 7A7 7 0 0 0 3.5 6M4 13a7 7 0 0 0 12.5 1" fill="none" stroke="#fff" stroke-width="2.2"/><path d="M17 2v6h-6M3 18v-6h6" fill="none" stroke="#fff" stroke-width="2"/></svg>
    <span class="navbar__title">Photo</span>
    <svg class="abs" style="left:200px;top:11px" width="20" height="20" viewBox="0 0 20 20"><circle cx="10" cy="10" r="7" fill="none" stroke="#fff" stroke-width="1.8"/><path d="M10 0v20M0 10h20" stroke="#fff" stroke-width="1.8"/></svg>
    <svg class="abs" style="left:246px;top:11px" width="20" height="20" viewBox="0 0 20 20"><circle cx="10" cy="10" r="10" fill="#fff"/><path d="M6.5 6.5l7 7M13.5 6.5l-7 7" stroke="#0d7af3" stroke-width="2.2"/></svg>
  </header>
  <div class="abs viewfinder"></div>
  <div class="abs capture" role="img" aria-label="Captured photo: dusk sky over mountains and a calm lake"></div>
  <div class="abs filters">
    <div class="filter filter--active"><div class="filter__thumb" style="background:linear-gradient(180deg,#a9866e,#3b302b)" role="img" aria-label="Filter preview"></div>example</div>
    <div class="filter"><div class="filter__thumb" style="background:linear-gradient(180deg,#8a7360,#2f2823)" role="img" aria-label="Filter preview"></div>example</div>
    <div class="filter"><div class="filter__thumb" style="background:linear-gradient(180deg,#b8654a,#4a261c)" role="img" aria-label="Filter preview"></div>example</div>
    <div class="filter"><div class="filter__thumb" style="background:linear-gradient(180deg,#b09a82,#4a3e34)" role="img" aria-label="Filter preview"></div>example</div>
    <div class="filter"><div class="filter__thumb" style="background:linear-gradient(180deg,#7fa396,#28423c)" role="img" aria-label="Filter preview"></div>example</div>
    <div class="filter"><div class="filter__thumb" style="background:linear-gradient(180deg,#a08aa8,#3a2c42)" role="img" aria-label="Filter preview"></div>example</div>
  </div>
  <div class="abs tools">
    <div class="tool" style="left:14px"><svg width="14" height="14" viewBox="0 0 14 14"><path d="M7 0v14M0 7h14" stroke="#0d7af3" stroke-width="2.4"/></svg></div>
    <div class="tool" style="left:63px"><svg width="20" height="20" viewBox="0 0 20 20"><circle cx="10" cy="10" r="4" fill="#0d7af3"/><path d="M10 1v3M10 16v3M1 10h3M16 10h3M3.6 3.6l2.1 2.1M14.3 14.3l2.1 2.1M3.6 16.4l2.1-2.1M14.3 5.7l2.1-2.1" stroke="#0d7af3" stroke-width="1.8"/></svg></div>
    <div class="shutter"><span><svg width="26" height="21" viewBox="0 0 22 18"><rect x="1" y="4" width="20" height="13" rx="3" fill="#0d7af3"/><rect x="7" y="1" width="8" height="4" rx="1" fill="#0d7af3"/><circle cx="11" cy="10.5" r="4" fill="#fff"/><circle cx="11" cy="10.5" r="2.3" fill="#0d7af3"/></svg></span></div>
    <div class="tool" style="left:189px"><svg width="18" height="18" viewBox="0 0 18 18"><path d="M4 0v14h14M0 4h14v14" fill="none" stroke="#0d7af3" stroke-width="2"/><path d="M3 15L15 3" stroke="#0d7af3" stroke-width="1.5"/></svg></div>
    <div class="tool" style="left:238px"><svg width="14" height="18" viewBox="0 0 14 18"><path d="M7 0C5 5 1 8 1 12a6 6 0 0 0 12 0C13 8 9 5 7 0z" fill="#0d7af3"/></svg></div>
  </div>
</section>

</body>
</html>
```